Photography and Political Commentary Blog

Hi there!
I'd like to build a clean, simple, yet visually appealing blog using a theme similar to this: http://www.brightlayouts.net/demo/?theme=TheFrame. I’m looking to work with a designer who has a modern aesthetic who can work with me to create a great blog. Hopefully that’s you!
Details:
The aim would be for the blog to be simple and clean, with each post represented by a picture, title and short summary as with ‘The Frame’ theme. These post summaries would be displayed in a single area without sidebars or columns.
There would be a home page in addition to four pages that you can access from a menu panel. These subordinate pages would be very similar if not the same in style to the main page. The subordinate pages would be:
- Politics
- Security
- Photography
- Music
For each page:
Politics and Security. These pages would be in a traditional blog format with the ability to post, hyperlink, comment etc. Posts would typically be 200-400 words. I am in the military and actively involved in politics and would like to be able to post my thoughts on issues ‘Quick Thoughts on Big Ideas’, and hyperlink to articles with short personal comments.
Photography. The photography main page would be like the homepage with each post represented by a single photo, title and summary (as per ‘The Frame’ theme). The individual posts would need to be able to display photo galleries in a grid, with the ability to click on individual photos to view them in high definition. I am open to the use of different widgets to best display the photos. Typically, each gallery would have 6-10 photos. I am a keen amateur (semi-professional?) photographer. This page would showcase small galleries of my artistic work as opposed to large journal/travel style galleries.
Music. This page is a simply way for me to post links to songs I like from ClipNest, Reelo, Tunebarn etc.
I like the clean style and typeface of the following blogs:
http://www.gallowmark.com/
http://www.thecusp.com/
http://quenlatori.com/
http://hollyonstuffs.com/
http://whatmysisterpicked.jotpage.com/
I like color palates similar to these –
http://www.huevault.com/palette/482137/Moss_Heron
http://www.huevault.com/palette/2958/Cedar_Nine
The first file I have attached is a logo that uses the types of colors and look I'd like to achieve. The second file I have attached has the type of font I'd like to use (something in the 'Sans' family: http://www.typecrate.com/fonts/category/sans/
In general, I like the use of red highlights with other neutral tones (greys, blues etc) but I’m open to your ideas!
For the function of the blog, the homepage would be a sequential summary of the posts from each of the subsections (politics, security, photography and music). I'd like this to be grouped so you can see 3 or 4 of the most recent posts from each section - but I'm open to ideas. The main pages for each subsection would be the same: a sequential summary of the posts for that area. If using Wordpress, I would like to be able to do this automatically, for instance by allocating ‘categories’ to each post that sort the posts into their respective sections.
The site name will be gavinmarsh.com.au. Any logos or headings would be my name ‘Gavin Marsh’. I already own the domain name.
The main aim for this project is for it to be clean, simple and elegant (in a modern way). Something that people can open and easily navigate without clutter, yet is visually appealing.
Thanks for taking the time to read this brief and really looking forward to working with you!
Cheers!
Gav

```html
<!DOCTYPE html>
<html lang="en">
<head>
<meta charset="utf-8">
<title>Gavin Marsh</title>
<link rel="stylesheet" href="https://fonts.googleapis.com/css2?family=Oswald:wght@400;600;700&family=Open+Sans:wght@400;600;700&display=swap">
<style>
:root{
  --red:#d8302a;
  --red-dark:#b3221d;
  --ink:#2b2e33;
  --header:#262a30;
  --nav:#1c1f24;
  --page:#4a5566;
  --page-2:#3f4958;
  --card:#ffffff;
  --muted:#6b6f75;
  --footer:#23272d;
  --footer-text:#aeb3ba;
  --line:#3a3f47;
  --site-name:#f2f3f5;
}
*{box-sizing:border-box;margin:0;padding:0}
html,body{width:753px;height:1200px;overflow:hidden}
body{font-family:"Open Sans",Arial,sans-serif;background:var(--page);color:var(--ink);position:relative}

.site-header{position:absolute;left:0;top:0;width:753px;height:60px;background:var(--header);display:flex;align-items:center;justify-content:space-between;padding:0 75px}
.site-name{display:flex;align-items:center;gap:9px;font-family:"Open Sans",sans-serif;font-weight:600;font-size:22px;color:var(--site-name)}
.site-name .mark{width:12px;height:12px;background:var(--red);display:block}
.search{display:flex;align-items:center}
.search-field{width:100px;height:18px;background:#3a3f47;border:1px solid #4a5058;color:#9aa0a7;font-size:8px;padding:0 6px;line-height:16px}
.search-btn{width:18px;height:18px;background:var(--red);display:flex;align-items:center;justify-content:center}

.main-nav{position:absolute;left:0;top:60px;width:753px;height:28px;background:var(--nav);padding-left:75px;display:flex}
.main-nav a{font-family:"Oswald",sans-serif;font-size:11px;font-weight:600;color:#e8e8e8;text-decoration:none;text-transform:uppercase;padding:0 14px;line-height:28px}
.main-nav a.current{background:var(--red);color:#fff}

.hero{position:absolute;left:0;top:88px;width:753px;height:262px;background:radial-gradient(ellipse at 70% 35%,#6a4a3a 0%,#3f3a38 22%,transparent 40%),linear-gradient(180deg,#7fa8b8 0%,#9fc3cf 45%,#5d8fa3 100%)}
.hero-caption{position:absolute;left:75px;top:86px;width:250px;text-align:right}
.hero-title{display:inline-block;background:rgba(40,20,18,.75);color:#fff;font-family:"Oswald",sans-serif;font-size:15px;padding:4px 10px}
.hero-date{color:var(--red);font-size:9px;font-weight:700;margin-top:6px}
.hero-text{color:#fff;font-size:9px;line-height:13px;margin-top:4px;text-shadow:0 1px 2px rgba(0,0,0,.5)}
.hero-more{display:inline-block;margin-top:8px;background:var(--red);color:#fff;font-size:9px;font-weight:700;padding:4px 12px;border-radius:2px}
.hero-arrow{position:absolute;top:120px;width:16px;height:22px;background:rgba(0,0,0,.45);display:flex;align-items:center;justify-content:center}
.hero-arrow.prev{left:18px}.hero-arrow.next{right:18px}

.content{position:absolute;left:0;top:350px;width:753px;height:600px;background:linear-gradient(180deg,var(--page) 0%,var(--page-2) 100%)}
.post-grid{position:absolute;left:83px;top:72px;width:600px;display:grid;grid-template-columns:repeat(3,188px);column-gap:18px;row-gap:22px}
.post-card{background:var(--card);height:225px;padding:5px;box-shadow:0 2px 4px rgba(0,0,0,.3)}
.post-thumb{position:relative;height:78px}
.post-thumb .tag{position:absolute;right:0;top:0;width:0;height:0;border-left:24px solid transparent;border-top:24px solid var(--red)}
.post-thumb .caption{position:absolute;left:0;right:0;bottom:0;height:20px;background:rgba(0,0,0,.65);color:#fff;font-size:11px;line-height:20px;padding-left:6px}
.post-thumb .count{position:absolute;right:5px;bottom:4px;background:#e0b020;color:#222;font-size:7px;font-weight:700;padding:1px 3px}
.post-meta{color:var(--red);font-size:7px;font-weight:700;margin-top:8px}
.post-text{font-size:7px;line-height:10px;color:var(--muted);margin-top:4px}
.post-more{font-size:7px;color:var(--ink);font-weight:700;margin-top:6px}

.pagination{position:absolute;right:72px;top:558px;display:flex;align-items:center;gap:7px;font-family:"Oswald",sans-serif;color:#fff;font-size:18px}
.pagination .current{color:#fff;font-weight:700}
.pagination span{color:#dfe3e8}

.site-footer{position:absolute;left:0;top:950px;width:753px;height:250px;background:var(--footer);color:var(--footer-text)}
.footer-col{position:absolute;top:44px}
.footer-col h3{font-family:"Oswald",sans-serif;font-size:12px;color:#fff;letter-spacing:.5px;text-transform:uppercase;margin-bottom:10px}
.footer-col ul{list-style:none}
.footer-col li{font-size:7px;line-height:9px;margin-bottom:6px;padding-left:8px;position:relative}
.footer-col li::before{content:"";position:absolute;left:0;top:3px;width:3px;height:3px;background:var(--red)}
.social{position:absolute;left:75px;top:202px;display:flex;gap:4px}
.social span{width:13px;height:13px;display:block}
.copyright{position:absolute;right:75px;top:204px;font-size:7px;color:var(--footer-text)}
.footer-rule{position:absolute;left:75px;right:75px;top:190px;height:1px;background:var(--line)}
</style>
</head>
<body>

<header class="site-header">
  <div class="site-name"><span class="mark"></span>Gavin Marsh</div>
  <div class="search">
    <div class="search-field">Search</div>
    <div class="search-btn"><svg width="9" height="9" viewBox="0 0 10 10"><circle cx="4" cy="4" r="3" fill="none" stroke="#fff" stroke-width="1.5"/><line x1="6.2" y1="6.2" x2="9" y2="9" stroke="#fff" stroke-width="1.5"/></svg></div>
  </div>
</header>

<nav class="main-nav">
  <a class="current" href="#">Home</a>
  <a href="#">About</a>
  <a href="#">Politics</a>
  <a href="#">Entertainment</a>
  <a href="#">Technology</a>
  <a href="#">Education</a>
  <a href="#">Fashion</a>
  <a href="#">Contact</a>
</nav>

<section class="hero" role="img" aria-label="Featured photograph: close-up of water droplets on a surface with a blurred blue background">
  <div class="hero-caption">
    <div class="hero-title">Maecenas non lobortis lacus.</div>
    <div class="hero-date">Dec 10, 2012. Posted by Admin</div>
    <p class="hero-text">Sed ut perspiciatis unde omnis iste natus error sit voluptatem accusantium doloremque laudantium, totam rem aperiam, eaque ipsa quae ab illo inventore veritatis.</p>
    <span class="hero-more">More</span>
  </div>
  <div class="hero-arrow prev"><svg width="6" height="10" viewBox="0 0 6 10"><path d="M5 1 1 5l4 4" fill="none" stroke="#fff" stroke-width="1.5"/></svg></div>
  <div class="hero-arrow next"><svg width="6" height="10" viewBox="0 0 6 10"><path d="M1 1l4 4-4 4" fill="none" stroke="#fff" stroke-width="1.5"/></svg></div>
</section>

<main class="content">
  <div class="post-grid">
    <article class="post-card">
      <div class="post-thumb" role="img" aria-label="Post photograph: grassy landscape scene" style="background:linear-gradient(160deg,#9bb07a,#4f6a3a)">
        <span class="tag"></span><div class="caption">Quisque Placerat Erat</div><span class="count">12</span>
      </div>
      <div class="post-meta">Posted by Admin</div>
      <p class="post-text">Proin vitae justo lacinia, aliquet velit sed, cursus nibh. Morbi tempor felis eu ante dictum facilisis nec id urna.</p>
      <p class="post-text">Nullam placerat vitae nisi ac accumsan. Mauris egestas ligula at sodales porttitor.</p>
      <div class="post-more">More »</div>
    </article>
    <article class="post-card">
      <div class="post-thumb" role="img" aria-label="Post photograph: dark street scene" style="background:linear-gradient(160deg,#8a7d70,#2f2a26)">
        <span class="tag"></span><div class="caption">Quisque Placerat Erat</div><span class="count">12</span>
      </div>
      <div class="post-meta">Posted by Admin</div>
      <p class="post-text">Proin vitae justo lacinia, aliquet velit sed, cursus nibh. Morbi tempor felis eu ante dictum facilisis nec id urna.</p>
      <p class="post-text">Nullam placerat vitae nisi ac accumsan. Mauris egestas ligula at sodales porttitor.</p>
      <div class="post-more">More »</div>
    </article>
    <article class="post-card">
      <div class="post-thumb" role="img" aria-label="Post photograph: outdoor portrait in a garden" style="background:linear-gradient(160deg,#7f9a6a,#3d4b34)">
        <span class="tag"></span><div class="caption">Quisque Placerat Erat</div><span class="count">12</span>
      </div>
      <div class="post-meta">Posted by Admin</div>
      <p class="post-text">Proin vitae justo lacinia, aliquet velit sed, cursus nibh. Morbi tempor felis eu ante dictum facilisis nec id urna.</p>
      <p class="post-text">Nullam placerat vitae nisi ac accumsan. Mauris egestas ligula at sodales porttitor.</p>
      <div class="post-more">More »</div>
    </article>
    <article class="post-card">
      <div class="post-thumb" role="img" aria-label="Post photograph: clock tower at dusk" style="background:linear-gradient(160deg,#c9a66e,#5a4630)">
        <span class="tag"></span><div class="caption">Quisque Placerat Erat</div><span class="count">12</span>
      </div>
      <div class="post-meta">Posted by Admin</div>
      <p class="post-text">Proin vitae justo lacinia, aliquet velit sed, cursus nibh. Morbi tempor felis eu ante dictum facilisis nec id urna.</p>
      <p class="post-text">Nullam placerat vitae nisi ac accumsan. Mauris egestas ligula at sodales porttitor.</p>
      <div class="post-more">More »</div>
    </article>
    <article class="post-card">
      <div class="post-thumb" role="img" aria-label="Post photograph: black and white view of an ancient amphitheatre" style="background:linear-gradient(160deg,#c8c8c8,#5c5c5c)">
        <span class="tag"></span><div class="caption">Quisque Placerat Erat</div><span class="count">12</span>
      </div>
      <div class="post-meta">Posted by Admin</div>
      <p class="post-text">Proin vitae justo lacinia, aliquet velit sed, cursus nibh. Morbi tempor felis eu ante dictum facilisis nec id urna.</p>
      <p class="post-text">Nullam placerat vitae nisi ac accumsan. Mauris egestas ligula at sodales porttitor.</p>
      <div class="post-more">More »</div>
    </article>
    <article class="post-card">
      <div class="post-thumb" role="img" aria-label="Post photograph: red flowers on a light background" style="background:linear-gradient(160deg,#e8e2dc,#c45a48)">
        <span class="tag"></span><div class="caption">Quisque Placerat Erat</div><span class="count">12</span>
      </div>
      <div class="post-meta">Posted by Admin</div>
      <p class="post-text">Proin vitae justo lacinia, aliquet velit sed, cursus nibh. Morbi tempor felis eu ante dictum facilisis nec id urna.</p>
      <p class="post-text">Nullam placerat vitae nisi ac accumsan. Mauris egestas ligula at sodales porttitor.</p>
      <div class="post-more">More »</div>
    </article>
  </div>
  <div class="pagination"><span>«</span><span class="current">1</span><span>2</span><span>3</span><span>»</span></div>
</main>

<footer class="site-footer">
  <div class="footer-col" style="left:75px;width:160px">
    <h3>Recent Posts</h3>
    <ul>
      <li>Aenean pulvinar interdum quam</li>
      <li>Pellentesque quis venenatis turpis</li>
      <li>Suspendisse lacinia mollis</li>
      <li>Vestibulum cursus ornare ante</li>
      <li>Ut sed fauce eget tortor ultrices</li>
      <li>Ut sed fauce eget tortor ultrices</li>
    </ul>
  </div>
  <div class="footer-col" style="left:263px;width:180px">
    <h3>Recent Comments</h3>
    <ul>
      <li>In scelerisque tellus vel ligula convallis, ullamcorper hendrerit nibh blandit</li>
      <li>Praesent id dolor non lacus suscipit consectetur tincidunt</li>
      <li>Phasellus vulputate ipsum sed nibh mattis tristique</li>
      <li>Etiam tempus lorem sagittis, varius lectus dignissim aliquam nibh</li>
    </ul>
  </div>
  <div class="footer-col" style="left:464px;width:120px">
    <h3>Blogroll</h3>
    <ul>
      <li>Documentation</li>
      <li>Plugins</li>
      <li>Suggest Ideas</li>
      <li>Support Forum</li>
      <li>Themes</li>
      <li>Dev Blog</li>
      <li>Dev Planet</li>
    </ul>
  </div>
  <div class="footer-col" style="left:602px;width:90px">
    <h3>Meta</h3>
    <ul>
      <li>Log in</li>
      <li>Entries RSS</li>
      <li>Comments RSS</li>
      <li>Site Home</li>
    </ul>
  </div>
  <div class="footer-rule"></div>
  <div class="social" aria-label="Social links">
    <span style="background:#3b5b99" aria-label="Social profile"></span>
    <span style="background:#3fa9e0" aria-label="Social profile"></span>
    <span style="background:#8a8f96" aria-label="Social profile"></span>
    <span style="background:#e07b20" aria-label="Feed"></span>
    <span style="background:#c0392b" aria-label="Social profile"></span>
    <span style="background:#5a6a7a" aria-label="Email"></span>
  </div>
  <div class="copyright">© 2014 gavinmarsh.com.au. All rights reserved</div>
</footer>

</body>
</html>
```